Advertisement Design Project

Attached is the information I need in a big color ad

10X11 that will go in a weekly local paper.
I am open to color and graphics-no pictures of people please.

My logo is also attached, which I would like in the ad.

Sorry for the short notice-I just got a deal on the space and it is due Friday.

```html
<!DOCTYPE html>
<html lang="en">
<head>
<meta charset="utf-8">
<title>Trusts, New Tax Laws – Estate Planning Workshop</title>
<link href="https://fonts.googleapis.com/css2?family=Oswald:wght@600;700&family=Roboto+Condensed:ital,wght@0,300;0,400;0,700;1,700&display=swap" rel="stylesheet">
<style>
  :root {
    --orange: #f8b133;
    --orange-soft: #fcd27c;
    --orange-pale: #fee6b4;
    --ink: #26313a;
    --navy: #1d2944;
    --text: #2b2b2b;
    --paper: #ffffff;
    --art-warm: #c9a77a;
    --art-green: #b7c4a2;
  }
  * { box-sizing: border-box; margin: 0; padding: 0; }
  html, body { width: 1091px; height: 1200px; overflow: hidden; background: var(--paper); }
  .ad {
    position: relative; width: 1091px; height: 1200px; overflow: hidden;
    background: var(--paper);
    font-family: "Roboto Condensed", "Arial Narrow", sans-serif; color: var(--text);
  }
  .backdrop { position: absolute; inset: 0; }
  .headline {
    position: absolute; top: 28px; left: 0; width: 100%; text-align: center;
    font-family: "Oswald", "Arial Narrow", sans-serif; font-weight: 700; line-height: 1; z-index: 2;
  }
  .headline .main { display: block; font-size: 108px; color: var(--ink); letter-spacing: -1px; }
  .headline .sub { display: block; font-size: 74px; color: var(--paper); margin-top: 2px; font-weight: 600; }
  .intro {
    position: absolute; top: 318px; left: 278px; font-size: 39px; font-weight: 300; color: var(--ink); z-index: 2;
  }
  .hero-art {
    position: absolute; left: 40px; top: 385px; width: 490px; height: 440px; z-index: 1;
    border-radius: 40% 40% 48% 48%;
    background: radial-gradient(ellipse at 50% 45%, #e9e2d3 0%, var(--art-green) 38%, var(--art-warm) 66%, rgba(255,255,255,0) 72%);
  }
  .questions { position: absolute; left: 558px; top: 380px; list-style: none; z-index: 2; }
  .questions li {
    position: relative; padding-left: 32px; height: 36.6px; line-height: 30px;
    font-size: 23px; font-weight: 700; font-style: italic; color: var(--text); white-space: nowrap;
  }
  .questions li::before {
    content: ""; position: absolute; left: 0; top: 6px; width: 18px; height: 18px;
    border-radius: 50%; background: var(--orange);
  }
  .workshop { position: absolute; left: 553px; top: 830px; font-size: 20px; line-height: 36px; color: var(--text); z-index: 2; }
  .workshop .label { font-size: 24px; font-weight: 700; font-style: italic; color: var(--orange); line-height: 32px; }
  .presenter { position: absolute; left: 59px; top: 848px; font-size: 20px; line-height: 36px; color: var(--text); z-index: 2; }
  .presenter .name, .presenter .role { font-size: 24px; font-weight: 700; font-style: italic; }
  .values {
    position: absolute; left: 56px; top: 1049px; width: 420px; height: 32px;
    background: var(--paper); border-radius: 16px;
    display: flex; align-items: center; justify-content: center; gap: 14px;
    font-size: 23px; font-weight: 700; font-style: italic; color: var(--ink);
  }
  .values .dot { width: 15px; height: 15px; border-radius: 50%; background: var(--orange); }
  .brand {
    position: absolute; left: 484px; top: 1070px; width: 120px; height: 120px; border-radius: 50%;
    background: var(--paper); display: flex; align-items: center; justify-content: center; text-align: center;
    font-size: 20px; font-weight: 700; color: var(--orange); line-height: 1.1;
  }
  .motto { position: absolute; left: 59px; top: 1122px; font-size: 18px; font-weight: 700; font-style: italic; color: var(--navy); line-height: 29px; }
  .reserve { position: absolute; right: 56px; top: 1118px; text-align: right; font-size: 21px; color: var(--navy); line-height: 31px; }
  .reserve .phone { font-size: 27px; font-weight: 700; font-style: italic; }
</style>
</head>
<body>
<div class="ad">
  <svg class="backdrop" width="1091" height="1200" viewBox="0 0 1091 1200" aria-hidden="true">
    <path d="M0 0 H1091 V205 Q545 372 0 205 Z" fill="var(--orange-soft)"/>
    <path d="M0 0 H1091 V190 Q545 355 0 190 Z" fill="var(--orange)"/>
    <path d="M0 680 C160 860 420 980 1091 1030 V1200 H0 Z" fill="var(--orange-pale)"/>
    <path d="M0 740 C170 900 440 1010 1091 1060 V1200 H0 Z" fill="var(--orange-soft)"/>
    <rect x="0" y="1100" width="1091" height="100" fill="var(--orange)"/>
  </svg>

  <h1 class="headline">
    <span class="main">Trusts, New Tax Laws</span>
    <span class="sub">Annuities and Long Term Care</span>
  </h1>

  <div class="hero-art" role="img" aria-label="Model house with red roof in a bird's nest with dollar bills"></div>

  <p class="intro">Come learn what you need to know</p>

  <ul class="questions">
    <li>&nbsp;Is a living trust right for me?</li>
    <li>Does my existing Trust need to be changed?</li>
    <li>Why does Joint Tenancy create tax problems?</li>
    <li>I have a will, isn’t that enough?</li>
    <li>Why do I need powers of attorney?</li>
    <li>How much are inheritance taxes?</li>
    <li>What are the new Affordable Care Act taxes?</li>
    <li>How does Long Term Care insurance work?</li>
    <li>How does Long Term Care insurance work?</li>
    <li>how do I plan for those costs?</li>
    <li>The truth about annuites-</li>
    <li>What are the biggest mistakes in estate planning?</li>
  </ul>

  <div class="workshop">
    <p class="label">Workshop</p>
    <p>on September 19, 2013</p>
    <p>at 1-2:30pm &amp;&nbsp; 6-7:30pm</p>
    <p>Venue : Bayview Shore Inn Aptos</p>
    <p>4200 Cliffside Way, Aptos, California 95003</p>
  </div>

  <div class="presenter">
    <p>Presented by:</p>
    <p class="name">Dana Ellis Marlow</p>
    <p class="role">Attorney at Law</p>
    <p>2150 Harbor Lane, Soquel.</p>
    <p>Helping&nbsp; Families plan their estates for over 20 years.</p>
  </div>

  <div class="values">
    <span>Trust</span><span class="dot"></span><span>Relationship</span><span class="dot"></span><span>Integrity</span>
  </div>

  <div class="brand">Marlow<br>Law</div>

  <div class="motto">
    <p>Security =Good information+Good Planning</p>
    <p>Be Smart. Plan Ahead.</p>
  </div>

  <div class="reserve">
    <p>Seating is limited for a Reservation,</p>
    <p>Please call: <span class="phone">(831) 555 - 0142</span></p>
  </div>
</div>
</body>
</html>
```